eBook Cover Design Project - Winter Lantern Vows

We need an ebook cover design for our new digital only title for Marigold Press.

Marigold Press is Romance. Marigold will own Romance in digital-first as Velvetine owns Romance in print and ebook.

We are looking for FUN, MODERN, PREMIUM designs. Please keep the look clean and edgy but have fun with it; be flirty - it's romance!!!

Target Market(s)

30-55 year old women.

Industry/Entity Type

Digital

Requirements
Must have
• Must work as a black and white image as well as a colour image.
- Must be easily viewed at thumbnail size.
- Title must always be larger than the author name. Both must appear on cover.
- Final file should be a JPEG supplied at 2240 pixels (H) X 1400 pixels (W).
- See attached document for story report.
- If using people on the cover refer to character traits in story report.
Should not have
• Offensive or pornographic content.
- Too many elements – keep it simple.

```html
<!DOCTYPE html>
<html lang="en">
<head>
<meta charset="utf-8">
<title>Winter Lantern Vows — Cover</title>
<link rel="stylesheet" href="https://fonts.googleapis.com/css2?family=Cinzel:wght@400;600;700&family=Roboto+Slab:wght@700&display=swap">
<style>
  :root {
    --ink: #0c0708;
    --shadow-brown: #2a1c18;
    --skin-warm: #b88e80;
    --haze-red: #b3202c;
    --deep-red: #6e0f18;
    --night: #1b1620;
    --ice: #e6f4fb;
    --ice-edge: #7fa6bb;
    --glow: #ff2a3c;
    --band-dark: #9c1620;
    --band-light: #f2a2a2;
    --white: #ffffff;
  }
  * { margin: 0; padding: 0; box-sizing: border-box; }
  html, body { width: 867px; height: 1200px; overflow: hidden; background: var(--ink); }
  .cover {
    position: relative;
    width: 867px;
    height: 1200px;
    overflow: hidden;
  }
  .cover-photo {
    position: absolute;
    inset: 0;
    background:
      linear-gradient(180deg, rgba(0,0,0,0) 0%, rgba(0,0,0,0) 35%, rgba(179,32,44,0.75) 42%, rgba(179,32,44,0.7) 58%, rgba(27,22,32,0.6) 68%, rgba(0,0,0,0) 76%),
      radial-gradient(ellipse 55% 30% at 30% 20%, var(--skin-warm) 0%, rgba(184,142,128,0) 70%),
      radial-gradient(ellipse 45% 25% at 80% 92%, #e2cfc8 0%, rgba(226,207,200,0) 70%),
      linear-gradient(180deg, var(--shadow-brown) 0%, #4a2f28 30%, var(--deep-red) 50%, var(--night) 72%, #111 100%);
  }
  .title {
    position: absolute;
    left: 0;
    width: 100%;
    text-align: center;
    font-family: 'Cinzel', serif;
  }
  .title-line-one {
    top: 440px;
    font-size: 84px;
    font-weight: 600;
    color: var(--ice);
    letter-spacing: 1px;
    text-shadow: 1px 1px 0 var(--ice-edge), 2px 2px 0 #5c7f92, 3px 3px 6px rgba(0,0,0,0.6);
  }
  .title-line-two {
    top: 612px;
    font-size: 120px;
    font-weight: 700;
    color: var(--ink);
    text-shadow: 0 0 14px var(--glow), 0 0 28px var(--glow), 0 0 44px rgba(255,42,60,0.7);
  }
  .author-band {
    position: absolute;
    left: 0;
    top: 1082px;
    width: 100%;
    height: 64px;
    background: linear-gradient(90deg, var(--band-dark) 0%, #c9434a 45%, var(--band-light) 100%);
    opacity: 0.92;
  }
  .author-name {
    position: absolute;
    left: 0;
    width: 100%;
    top: 1088px;
    text-align: center;
    font-family: 'Roboto Slab', serif;
    font-weight: 700;
    font-size: 44px;
    color: var(--white);
    padding-right: 30px;
  }
</style>
</head>
<body>
  <main class="cover">
    <div class="cover-photo" role="img" aria-label="Photograph of a dark-haired romantic couple embracing, bathed in red light"></div>
    <h1>
      <span class="title title-line-one">Winter Lantern</span>
      <span class="title title-line-two">Vows</span>
    </h1>
    <div class="author-band"></div>
    <p class="author-name">Nessa Calloway</p>
  </main>
</body>
</html>
```